GLOW ON THE AVENUE WEBSITE

I have a website www.glowontheavenue.org , need information from that jazzed up. wanted page to be fun & funky .

Target Market(s)

18 to 35yrs guys & girls

Requirements
Must have
• use all photos on website, need to attached my brochure for printing

```html
<!DOCTYPE html>
<html lang="en">
<head>
<meta charset="utf-8">
<title>Glow on the Avenue</title>
<link rel="stylesheet" href="https://fonts.googleapis.com/css2?family=Didact+Gothic&family=Open+Sans:wght@400;700&display=swap">
<style>
:root{
  --purple-light:#c6a6e2;
  --purple:#a47ccb;
  --purple-deep:#8a58ae;
  --heading-accent:#a27fcb;
  --ink:#3a3a3a;
  --body-text:#4a4a4a;
  --page:#f6f5f7;
  --top-bar:#3b3b3b;
  --footer-top:#474747;
  --footer-bottom:#262626;
  --footer-base:#1f1f1f;
  --footer-head:#c9c9c9;
  --footer-link:#bdbdbd;
  --thumb-border:#dcdcdc;
}
*{box-sizing:border-box;margin:0;padding:0}
html,body{width:1200px;height:1162px;overflow:hidden}
body{background:var(--page);font-family:"Didact Gothic",sans-serif;position:relative}
.top-bar{position:absolute;left:0;top:0;width:1200px;height:8px;background:var(--top-bar)}
.flower-backdrop{position:absolute;left:0;top:8px;width:360px;height:370px;
  background:radial-gradient(ellipse at 25% 35%,#e4d8f1 0%,#efe9f6 45%,rgba(246,245,247,0) 80%)}
.hero-photo{position:absolute;left:355px;top:8px;width:845px;height:378px;
  background:linear-gradient(180deg,#f3f1f4 0%,#e9c9a8 45%,#e8953c 72%,#f4f2f5 100%)}
.brand-tab{position:absolute;left:100px;top:0;width:201px;height:115px;
  background:linear-gradient(180deg,var(--purple-light),var(--purple-deep));
  border:2px solid #fff;border-top:none;border-radius:0 0 12px 12px;
  display:flex;align-items:flex-end;justify-content:center;padding:0 10px 22px;
  box-shadow:0 2px 6px rgba(0,0,0,.15)}
.brand-tab span{color:#fff;font-size:22px;line-height:1.05;text-align:center}
.side-nav{position:absolute;left:103px;top:173px;width:251px;height:422px;
  background:linear-gradient(180deg,var(--purple-light) 0%,var(--purple) 50%,var(--purple-deep) 100%);
  border:2px solid #fff;border-radius:8px;box-shadow:0 1px 5px rgba(0,0,0,.15)}
.side-nav ul{list-style:none;position:absolute;left:0;top:16px;width:100%}
.side-nav li{height:32px;line-height:32px;padding-left:24px;color:#fff;font-size:15px;position:relative}
.side-nav li::before{content:"";position:absolute;left:14px;top:12px;border-left:4px solid #fff;border-top:4px solid transparent;border-bottom:4px solid transparent}
.side-nav li.is-active{color:#fff}
.active-ribbon{position:absolute;left:91px;top:190px}
.side-nav li.is-active{z-index:2}
.welcome-title{position:absolute;left:370px;top:412px;font-size:43px;font-weight:400;color:var(--ink);letter-spacing:.5px;white-space:nowrap}
.welcome-title em{font-style:normal;color:var(--heading-accent)}
.welcome-copy{position:absolute;left:370px;top:483px;width:728px;font-family:"Open Sans",sans-serif;font-size:14.3px;line-height:22px;color:var(--body-text);text-align:justify}
.gallery{position:absolute;top:637px;left:0;width:1200px}
.gallery-item{position:absolute;top:0;width:299px;height:183px;border:3px solid var(--thumb-border)}
.gallery-item.one{left:107px;background:linear-gradient(135deg,#c89a7c,#f1e3da 55%,#e9e4e0)}
.gallery-item.two{left:446px;background:linear-gradient(180deg,#6a7a9c,#c8a3b3 45%,#e7b69a 60%,#7c8fb1)}
.gallery-item.three{left:783px;background:linear-gradient(180deg,#fbf3f4,#f2c9b0 55%,#d99a8f 80%,#fbeeee)}
.site-footer{position:absolute;left:0;top:896px;width:1200px;height:192px;
  background:linear-gradient(180deg,var(--footer-top),var(--footer-bottom))}
.footer-col{position:absolute;top:34px;padding-right:20px}
.footer-col h3{font-family:"Open Sans",sans-serif;font-weight:700;font-size:18px;color:var(--footer-head);margin-bottom:6px}
.footer-col a{display:block;color:var(--footer-link);font-family:"Open Sans",sans-serif;font-size:13px;line-height:16.6px;text-decoration:none}
.footer-divider{position:absolute;top:30px;width:1px;height:140px;background:rgba(0,0,0,.25);box-shadow:1px 0 0 rgba(255,255,255,.05)}
.footer-base{position:absolute;left:0;top:1088px;width:1200px;height:74px;background:var(--footer-base)}
.footer-brand{position:absolute;left:110px;top:22px;font-size:24px;color:#bdbdbd}
.copyright{position:absolute;left:460px;top:34px;font-family:"Open Sans",sans-serif;font-weight:700;font-size:11px;color:#a8a8a8}
.social{position:absolute;left:937px;top:17px;display:flex;gap:5px}
.social span{width:36px;height:36px;border-radius:50%;background:#5a5a5a;display:block}
</style>
</head>
<body>
<div class="top-bar"></div>
<div class="flower-backdrop" role="img" aria-label="Soft lavender crocus flowers"></div>
<div class="hero-photo" role="img" aria-label="Woman lying on an orange towel, showing smooth legs"></div>

<div class="brand-tab"><span>Glow on the Avenue</span></div>

<nav class="side-nav">
  <ul>
    <li class="is-active">Wecome</li>
    <li>Waxing</li>
    <li>City brow bar</li>
    <li>Eyes incl. Lash extensions</li>
    <li>Tanning</li>
    <li>Hand &amp; Feet</li>
    <li>Facials &amp; Massage</li>
    <li>Makeup</li>
    <li>Specials</li>
    <li>Products</li>
    <li>Blog</li>
    <li>Contact Us</li>
  </ul>
</nav>
<svg class="active-ribbon" width="224" height="32" viewBox="0 0 224 32" aria-hidden="true">
  <polygon points="0,0 205,0 222,16 205,31 0,31" fill="#3e3e3e"/>
  <polygon points="27,12 31,16 27,20" fill="#fff"/>
  <text x="38" y="21" fill="#fff" font-family="Didact Gothic, sans-serif" font-size="15">Wecome</text>
</svg>

<h1 class="welcome-title"><em>Welcome To</em> Glow on the Avenue</h1>
<p class="welcome-copy">simply dummy text of the printing and typesetting industry. Lorem Ipsum has been the industry's standard dummy text ever since the 1500s, when an unknown printer took a galley of type and scrambled it to make a type specimen book. It has survived not only five centuries, but also the leap into electronic typesetting, remaining essentially unchanged. It was popularised in the 1960s with the release of Letraset sheets containing Lorem Ipsum passages, and more recently with desktop publishing software</p>

<div class="gallery">
  <div class="gallery-item one" role="img" aria-label="Wax strip being applied to a leg"></div>
  <div class="gallery-item two" role="img" aria-label="Body silhouette against a pink sunset sky over water"></div>
  <div class="gallery-item three" role="img" aria-label="Legs with pink gerbera flowers reflected in water"></div>
</div>

<footer class="site-footer">
  <div class="footer-col" style="left:110px"><h3>Solutions</h3><a>Send Large Files</a><a>Fileshare</a><a>CloudCrate Alternative</a><a>Online Storage</a></div>
  <div class="footer-divider" style="left:278px"></div>
  <div class="footer-col" style="left:320px"><h3>Verticals</h3><a>Architecture</a><a>Media &amp; Entertainment</a><a>Legal Firms</a><a>Creative agencies</a><a>Creators</a></div>
  <div class="footer-divider" style="left:507px"></div>
  <div class="footer-col" style="left:549px"><h3>Apps &amp; Plugins</h3><a>Desktop App</a><a>Mobile Tools</a><a>Web App</a><a>Express for Desktop</a><a>Inboxly Plugin</a><a>Mailpost App</a></div>
  <div class="footer-divider" style="left:734px"></div>
  <div class="footer-col" style="left:775px"><h3>Partnerships</h3><a>Developers</a><a>Affiliates</a><a>Referral</a><a>Resellers</a></div>
  <div class="footer-divider" style="left:937px"></div>
  <div class="footer-col" style="left:978px"><h3>Help Center</h3><a>Support</a><a>User Forums</a><a>Flight School</a><a>Community</a><a>Report Abuse</a></div>
</footer>
<div class="footer-base">
  <div class="footer-brand">Glow on the Avenue</div>
  <div class="copyright">Copyrights © 2013 BoxVault. All rights reserved.</div>
  <div class="social" aria-label="Social links"><span></span><span></span><span></span><span></span></div>
</div>
</body>
</html>
```